Project Overview:
We are looking to create a website for a monthly subscription IPTV service in WordPress. The website should provide a seamless user experience for customers to sign up for the service and manage their account information. We need the following pages: Home Page, Product Page, Sign-Up Page, and Account Information Page.

Home Page:
The Home Page design should be simple and clean, with a dark theme and minimalistic design elements. We would like to include graphics of popular movie shows displayed on multiple devices. The page should highlight the key benefits and features of our service and provide a clear call-to-action for visitors to sign up.

Product Page:
The Product Page should provide detailed information about our subscription tiers and pricing plans. It should highlight the key features of each plan and provide a clear comparison between them. The page should also include a call-to-action button for visitors to sign up.

Sign-Up Page:
The Sign-Up Page is the conversion page where members will sign up for the service. It should collect the following information: Name, Phone Number, Email, Password, and Payment Information. The design should be simple, intuitive, and easy to use. It should highlight the benefits of our service and provide a clear call-to-action for visitors to sign up.

Account Information Page:
The Account Information Page should allow members to view and manage their account details. It should include the following information: Profile Image, Contact Details, Password Management, Payment Information Management, and Membership Expiration Date. The design should be user-friendly, intuitive, and easy to navigate.

Goals: The primary goal of the website is to provide an easy-to-use portal for customers to sign up for the service and manage their account information. The website should be user-friendly and visually appealing to attract potential customers.

Scope: The scope of the project includes designing a home page, a sign-up page, an account information page, and a payment information page. The website should be designed to be responsive and accessible on desktop and mobile devices.

Design Preferences: The design should be clean, modern, and visually appealing. The use of a color palette that is consistent with the brand identity is recommended. The website should be easy to navigate and provide a clear call-to-action for users to sign up for the service.

FYI: The subscription service I am designing a website for is related to an IPTV service. IPTV stands for Internet Protocol Television, which is a digital television broadcasting protocol that uses the internet to deliver TV programs and videos to viewers. The website will allow customers to sign up for the IPTV service and access their account information such as user name and password, membership tier, name, and payment details. Please let me know if you have any further questions, and I would be happy to provide more details. Thank you!

Dear Designers,

Thank you for your participation in our project. After reviewing the designs received so far, we have decided to update the brief to better reflect our needs and preferences. We apologize for any confusion this may cause, but we believe that these changes will result in better design submissions and a more successful project overall.

The updated brief is as follows:

We are looking to create a website for WordPress.

Also, here is the updated Brief.

Project Title: WordPress Website Design for Monthly Subscription IPTV Service

Project Overview:
We are looking to create a website for a monthly subscription IPTV service. The website should provide a seamless user experience for customers to sign up for the service and manage their account information. We need the following pages: Home Page, Product Page, Sign-Up Page, and Account Information Page.

Home Page:

Product Page:

Sign-Up Page:

Account Information Page:

Design Preferences:
We prefer a dark theme with minimalistic design elements and hits of our logo colors. The website should be easy to use and navigate, with clear calls-to-action and simple, intuitive forms. The design should be optimized for mobile devices and load quickly.

We hope that these updates provide you with a clearer understanding of our requirements and preferences. Please let us know if you have any questions or concerns. We look forward to seeing your revised designs.

Thank you again for your participation.
We will guarantee this project as soon as we see something we like that meets the updated requirements.

The website's target audience is individuals who are interested in subscribing to the monthly service.

• One item for sale and a client profile section.

```html
<!DOCTYPE html>
<html lang="en">
<head>
<meta charset="utf-8">
<title>VIEWORA – Unlimited Movies, TV Shows and More</title>
<link rel="stylesheet" href="https://fonts.googleapis.com/css2?family=Ubuntu:wght@400;500;700&display=swap">
<style>
:root{
  --red:#e00024;
  --red-line:#d6112f;
  --black:#000;
  --field:#141414;
  --white:#fff;
  --ink:#111;
  --text:#222;
  --muted:#444;
  --tick:#1a8fe3;
  --crimson:#c7354f;
  --rule:#dcdcdc;
}
*{box-sizing:border-box;margin:0;padding:0}
html,body{width:1200px;height:2322px;overflow:hidden}
body{position:relative;font-family:"Ubuntu",sans-serif;background:var(--white);color:var(--text)}
.abs{position:absolute}

/* Hero */
.hero{position:absolute;left:0;top:0;width:1200px;height:681px;
  background:radial-gradient(ellipse at 50% 40%,#4a4038 0%,#2a2623 45%,#121212 100%)}
.brand{position:absolute;font-family:"Ubuntu",sans-serif;font-weight:700;color:var(--red);letter-spacing:1px;display:flex;align-items:center;gap:8px}
.brand .mark{width:14px;height:14px;background:var(--red)}
.hero .brand{left:52px;top:26px;font-size:40px}
.btn-signin{position:absolute;left:973px;top:41px;width:128px;height:37px;border-radius:6px;background:var(--red);color:var(--white);font-size:18px;font-weight:500;display:flex;align-items:center;justify-content:center}
.signup-card{position:absolute;left:400px;top:79px;width:399px;height:547px;background:var(--black);border:1.5px solid var(--red-line);border-radius:45px}
.signup-card h1{position:absolute;left:0;top:22px;width:100%;text-align:center;font-size:31px;font-weight:700;line-height:41px;color:var(--white)}
.signup-card h2{position:absolute;left:27px;top:134px;font-size:25px;font-weight:500;color:var(--white)}
.field{position:absolute;left:27px;width:344px;height:47px;background:var(--field);border-radius:6px;color:var(--white);font-size:13px;display:flex;align-items:center;justify-content:space-between;padding:0 13px 0 15px}
.field svg{width:12px;height:12px}
.btn-signup{position:absolute;left:27px;top:364px;width:344px;height:47px;border-radius:5px;background:var(--red);color:var(--white);font-size:26px;font-weight:500;display:flex;align-items:center;justify-content:center}
.pay-title{position:absolute;left:28px;top:430px;font-size:20px;font-weight:500;color:var(--white)}
.pay-row{position:absolute;left:28px;top:465px;display:flex;gap:9px}
.pay-card{width:60px;height:42px;border-radius:4px;color:var(--white);font-size:11px;font-weight:500;display:flex;align-items:center;justify-content:center}

/* Service */
.service-frame{position:absolute;left:81px;top:801px;width:505px;height:511px;border:1.5px solid var(--red-line);border-radius:45px}
.service-photo{position:absolute;left:98px;top:783px;width:506px;height:513px;border-radius:45px;
  background:linear-gradient(180deg,#2a2522 0%,#3b3530 45%,#6b5a4c 70%,#1d1d1d 100%)}
.service-title{position:absolute;left:685px;top:788px;font-size:43px;font-weight:500;color:var(--ink)}
.features{position:absolute;left:686px;top:870px;list-style:none}
.features li{height:44.8px;display:flex;align-items:center;gap:20px;font-size:20px;color:var(--text)}
.features svg{width:20px;height:20px}
.btn-access{position:absolute;left:693px;top:1225px;width:310px;height:57px;border-radius:29px;background:var(--red);color:var(--white);font-size:19px;font-weight:500;display:flex;align-items:center;justify-content:center}

/* Channels */
.channels{position:absolute;left:0;top:1388px;width:1200px;height:603px;
  background:linear-gradient(100deg,#cc3a55 0%,#c5324d 45%,#a8394c 75%,#8c3141 100%)}
.channels h3{position:absolute;font-size:43px;font-weight:500;color:var(--white)}
.free-grid{position:absolute;left:111px;top:138px;display:grid;grid-template-columns:repeat(4,97px);grid-auto-rows:97px;column-gap:16px;row-gap:5px}
.tile{border:3px solid #111;display:flex;align-items:center;justify-content:center;font-weight:700;font-size:20px}
.tile.light{background:var(--white);color:#111}
.tile.tint{background:rgba(255,150,170,.35);color:#113}
.paid-box{position:absolute;left:637px;top:313px;width:465px;height:234px;background:var(--white);border:2px solid var(--red-line);display:grid;grid-template-columns:repeat(5,1fr);grid-template-rows:repeat(3,1fr);padding:8px 10px}
.paid-box span{display:flex;align-items:center;justify-content:center;text-align:center;font-size:14px;font-weight:700;color:#1a1a1a}

/* Subscription + footer */
.sub-title{position:absolute;left:98px;top:2066px;font-size:43px;font-weight:500;color:var(--ink)}
.sub-note{position:absolute;left:99px;top:2124px;font-size:15px;color:var(--muted)}
.sub-input{position:absolute;left:555px;top:2076px;width:304px;height:63px;border:1.5px solid #ddd;border-radius:10px;background:var(--white)}
.btn-subscribe{position:absolute;left:889px;top:2077px;width:213px;height:62px;border-radius:10px;background:var(--red);color:var(--white);font-size:26px;font-weight:500;display:flex;align-items:center;justify-content:center}
.rule{position:absolute;left:98px;top:2204px;width:1004px;height:1px;background:var(--rule)}
.footer .brand{left:101px;top:2228px;font-size:42px}
.copyright{position:absolute;right:102px;top:2241px;font-size:16px;color:var(--ink)}
</style>
</head>
<body>

<header class="hero" role="img" aria-label="Curved wall of TV screens showing movies and shows">
</header>
<div class="abs brand-wrap">
  <div class="brand" style="left:52px;top:26px;font-size:40px"><span class="mark"></span>VIEWORA</div>
</div>
<div class="btn-signin">Sign In</div>

<section class="signup-card">
  <h1>Unlimited Movies TV<br>Shows And More</h1>
  <h2>Sign Up</h2>
  <div class="field" style="top:182px">User Name
    <svg viewBox="0 0 12 12"><circle cx="6" cy="3.5" r="2.5" fill="#fff"/><path d="M1.5 11.5c0-3 2-4.5 4.5-4.5s4.5 1.5 4.5 4.5z" fill="#fff"/></svg>
  </div>
  <div class="field" style="top:242px">Password
    <svg viewBox="0 0 12 12"><path d="M.5 6C2 3.5 4 2.5 6 2.5S10 3.5 11.5 6C10 8.5 8 9.5 6 9.5S2 8.5.5 6z" fill="none" stroke="#fff" stroke-width="1.3"/><circle cx="6" cy="6" r="1.8" fill="#fff"/><path d="M2 10.5 10 1.5" stroke="#fff" stroke-width="1.2"/></svg>
  </div>
  <div class="field" style="top:298px">Membership Tier
    <svg viewBox="0 0 12 12"><path d="M3 4.5 6 7.5 9 4.5" fill="none" stroke="#fff" stroke-width="1.5"/></svg>
  </div>
  <div class="btn-signup">Sign Up</div>
  <div class="pay-title">Payment Details</div>
  <div class="pay-row">
    <div class="pay-card" style="background:#253b80">PayNest</div>
    <div class="pay-card" style="background:#1a5cb0">Vela</div>
    <div class="pay-card" style="background:#3b4a5c">Cirqa</div>
    <div class="pay-card" style="background:#1f72cd">Orbex</div>
  </div>
</section>

<div class="service-frame"></div>
<div class="service-photo" role="img" aria-label="Family on a sofa watching a football match on a wall-mounted TV"></div>
<h2 class="service-title">BEST IPTV SERVICE</h2>
<ul class="features">
  <li><svg viewBox="0 0 20 20"><circle cx="10" cy="10" r="9" fill="var(--tick)"/><path d="M5.5 10.3 8.6 13.2 14.5 7" fill="none" stroke="#fff" stroke-width="2.2"/></svg>Nemo enim ipsam voluptatem quia</li>
  <li><svg viewBox="0 0 20 20"><circle cx="10" cy="10" r="9" fill="var(--tick)"/><path d="M5.5 10.3 8.6 13.2 14.5 7" fill="none" stroke="#fff" stroke-width="2.2"/></svg>Nemo enim ipsam voluptatem quia</li>
  <li><svg viewBox="0 0 20 20"><circle cx="10" cy="10" r="9" fill="var(--tick)"/><path d="M5.5 10.3 8.6 13.2 14.5 7" fill="none" stroke="#fff" stroke-width="2.2"/></svg>Nemo enim ipsam voluptatem quia</li>
  <li><svg viewBox="0 0 20 20"><circle cx="10" cy="10" r="9" fill="var(--tick)"/><path d="M5.5 10.3 8.6 13.2 14.5 7" fill="none" stroke="#fff" stroke-width="2.2"/></svg>Nemo enim ipsam voluptatem quia</li>
  <li><svg viewBox="0 0 20 20"><circle cx="10" cy="10" r="9" fill="var(--tick)"/><path d="M5.5 10.3 8.6 13.2 14.5 7" fill="none" stroke="#fff" stroke-width="2.2"/></svg>Nemo enim ipsam voluptatem quia</li>
  <li><svg viewBox="0 0 20 20"><circle cx="10" cy="10" r="9" fill="var(--tick)"/><path d="M5.5 10.3 8.6 13.2 14.5 7" fill="none" stroke="#fff" stroke-width="2.2"/></svg>Nemo enim ipsam voluptatem quia</li>
  <li><svg viewBox="0 0 20 20"><circle cx="10" cy="10" r="9" fill="var(--tick)"/><path d="M5.5 10.3 8.6 13.2 14.5 7" fill="none" stroke="#fff" stroke-width="2.2"/></svg>Nemo enim ipsam voluptatem quia</li>
</ul>
<div class="btn-access">Get My IPTV Access now</div>

<section class="channels" role="img" aria-label="Red-tinted wall of TV screens with a hand holding a remote control">
  <h3 style="left:102px;top:58px">TOP FREE CHANNEL</h3>
  <div class="free-grid">
    <div class="tile light">PULSE</div><div class="tile light">PULSE</div><div class="tile light">PULSE</div><div class="tile light">PULSE</div>
    <div class="tile tint">Kidora</div><div class="tile tint">Kidora</div><div class="tile tint">Kidora</div><div class="tile tint">Kidora</div>
    <div class="tile tint">STELLA</div><div class="tile tint">STELLA</div><div class="tile tint">STELLA</div><div class="tile tint">STELLA</div>
  </div>
  <h3 style="left:637px;top:246px">TOP PAID CHANNEL</h3>
  <div class="paid-box">
    <span>modeTV</span><span>Late Hour</span><span>Vexa</span><span>QZ</span><span>Terra World</span>
    <span>HEROIK</span><span>HOMEHQ</span><span>The Meridian</span><span>NEWSLINE</span><span>Ward Seven</span>
    <span>Ch 12</span><span>ToonBay</span><span>Stage Quest</span><span>Loopz</span><span>Wavecast 4</span>
  </div>
</section>

<h2 class="sub-title">SUBSCRIPTION</h2>
<p class="sub-note">Lorem ipsum dolor sit amet, consectetur adipiscing elit</p>
<div class="sub-input"></div>
<div class="btn-subscribe">Subscribe</div>

<footer class="footer">
  <div class="rule"></div>
  <div class="brand"><span class="mark"></span>VIEWORA</div>
  <p class="copyright">© copyrights 2023 VIEWORA|&nbsp; All Rights Reserved</p>
</footer>

</body>
</html>
```